Business Card for New Greek Restaurant

Looking for a Business card for a new Greek Restaurant that's focus is on Take out and Delivery & catering.

Also to outline the contact information for the restaurant.
Does not require a name or title of a specific person (Just general business card)
Phone (519) 731-FOOD (3663)
Email : info@bluefigkitchen.ca
Website : www.bluefigkitchen.ca

Facebook/Instagram/Twitter Icons to Follow us as well.

TAKEOUT * DELIVERY* CATERING

Target Market(s)

Woman Age 25-44

Industry/Entity Type

Greek Restaurant

Contact Information for Business Card

Card is to have the general contact information for the business as well as outline our Take Out and Catering Services. Existing Logo attached and to be incorporated into the design.

Font styles to use
Sans Serif

Colors

Designer to choose colors to be used in the design.

Requirements
Must have
• Restaurant Contact Information :
• Phone (519) 731-FOOD (3663)
• Email : info@bluefigkitchen.ca
• Website : www.bluefigkitchen.ca
• Highlight Takeout, Catering, Delivery
• Business Address :
• Maplerow Plaza
• 47 Carden Ave., Unit 6
• Alderbrook ON
• N0K 2P5
Nice to have
• Modern Feel to promote TakeOut and Catering Services.
Should not have
• No Specific Title or Contact Person (Generic Business Card for Restaurant)

```html
<!DOCTYPE html>
<html lang="en">
<head>
<meta charset="utf-8">
<title>Blue Fig Kitchen – Business Card</title>
<link rel="stylesheet" href="https://fonts.googleapis.com/css2?family=Questrial&display=swap">
<style>
  :root {
    --stage: #3b3b3d;
    --brand-blue: #10aee4;
    --card-white: #f7f7f7;
    --pale-blue: #cfe3ef;
    --ink-white: #ffffff;
  }
  * { margin: 0; padding: 0; box-sizing: border-box; }
  html, body { width: 1200px; height: 900px; overflow: hidden; }
  body {
    background: var(--stage);
    font-family: "Questrial", "Century Gothic", sans-serif;
    position: relative;
  }
  .card {
    position: absolute;
    top: 150px;
    width: 360px;
    height: 600px;
    border-radius: 26px;
    overflow: hidden;
  }
  .card--front { left: 200px; background: var(--card-white); color: var(--brand-blue); }
  .card--back { left: 640px; background: var(--brand-blue); color: var(--ink-white); }

  .brand-name {
    font-size: 36px;
    font-weight: 400;
    line-height: 1.08;
    letter-spacing: 1px;
    text-transform: uppercase;
    position: absolute;
    top: 70px;
    width: 260px;
  }
  .card--front .brand-name { left: 62px; }
  .card--back .brand-name { left: 48px; }

  .divider {
    position: absolute;
    left: 62px;
    width: 80px;
    height: 3px;
    background: var(--brand-blue);
  }
  .divider--top { top: 232px; }
  .divider--bottom { top: 430px; }

  .contact-list {
    position: absolute;
    left: 62px;
    top: 262px;
    list-style: none;
    font-size: 17px;
    line-height: 1.55;
  }
  .contact-list li { display: flex; align-items: flex-start; gap: 10px; }
  .contact-list .icon { width: 15px; height: 15px; flex: none; margin-top: 5px; }
  .address-lines { display: block; }

  .website {
    position: absolute;
    left: 62px;
    bottom: 60px;
    font-size: 22px;
  }

  .services {
    position: absolute;
    left: 48px;
    top: 208px;
    font-size: 19px;
    letter-spacing: 0.5px;
  }
  .services .sep { margin: 0 8px; }

  .decor-area {
    position: absolute;
    right: 30px;
    bottom: 0;
    width: 150px;
    height: 330px;
    border-radius: 75px 75px 0 0;
    background: linear-gradient(180deg, var(--pale-blue), rgba(207, 227, 239, 0.55));
  }
</style>
</head>
<body>
  <section class="card card--front" aria-label="Business card front">
    <h1 class="brand-name">Blue Fig Kitchen</h1>
    <div class="divider divider--top"></div>
    <ul class="contact-list">
      <li>
        <svg class="icon" viewBox="0 0 16 16" aria-hidden="true"><path fill="currentColor" d="M3 1h3l1.5 4-2 1.3a9 9 0 0 0 4.2 4.2L11 8.5l4 1.5v3a2 2 0 0 1-2 2A12 12 0 0 1 1 3a2 2 0 0 1 2-2z"/></svg>
        <span>(555) 731-FOOD (3663)</span>
      </li>
      <li>
        <svg class="icon" viewBox="0 0 16 16" aria-hidden="true"><rect x="1" y="3" width="14" height="10" rx="1" fill="currentColor"/><path d="M1.5 3.5 8 9l6.5-5.5" fill="none" stroke="var(--card-white)" stroke-width="1.3"/></svg>
        <span>info@bluefigkitchen.ca</span>
      </li>
      <li>
        <svg class="icon" viewBox="0 0 16 16" aria-hidden="true"><path fill="currentColor" d="M8 0a5.5 5.5 0 0 1 5.5 5.5C13.5 10 8 16 8 16S2.5 10 2.5 5.5A5.5 5.5 0 0 1 8 0z"/><circle cx="8" cy="5.5" r="2" fill="var(--card-white)"/></svg>
        <span class="address-lines">Maplerow Plaza<br>47 Carden Ave., Unit 6<br>Alderbrook ON N0K 2P5</span>
      </li>
    </ul>
    <div class="divider divider--bottom"></div>
    <p class="website">www.bluefigkitchen.ca</p>
  </section>

  <section class="card card--back" aria-label="Business card back">
    <h2 class="brand-name">Blue Fig Kitchen</h2>
    <p class="services">Takeout<span class="sep">|</span>Catering<span class="sep">|</span>Delivery</p>
    <div class="decor-area" role="img" aria-label="Large pale brand emblem decoration"></div>
  </section>
</body>
</html>
```